Meadow Healers WEBSITE
Meadow Healers WEBSITE - Health
Creative Brief
Health
www.meadowhealers.example
This website will be used by medical doctors mainly in the United States and some from other parts of the world. These doctors all have lots of research and many years of experience with patients. We have a team of people writing a book and we want about 600 doctors to fill out a questionaire and write about their research for this book. They will be going to this website to learn about us, what we are doing, why it is important for them to be included in this book and then they will decide if they want to fill out the questionaires and upload their literature and their research to us. We need for them to watch a video . There will be a 4 minute video embedded for the front page and the content will be word press. You will receive this next week. Your development team will upload the video we will make. The doctors will send their info to our email address and they MUST agree to a "terms and conditions" or we will not accept their content. We will give each doctor the SAME password to use. They must fill out their name and email address in full in order for us to receive the information they send.
It needs to be simple yet modern and exciting. So yes, you can use for the places to click onto modern and fun styles. Whether it is carrots or asparagus or avocados or broccoli or beans or other vegetables that flash or outline a location move or whatever you come up with.. sure I am open to that. I just need a little more than any other website design. I want these doctors to fall in love with the professional website and of course the content and really want to be a part of this team and agree to be a part of this book they all deserve to be in. I want you to use all the photos I have uploaded. The "notebook photo" will go where the questionaire form is for them to fill out.
Modern
Soft Pale Green ... peaceful to the eyes
Soft Pale Blue peaceful to the eyes
Soft yellow, grey or magenta
top
www.brambletidecare.example
http://fernloftkitchen.example/
I put brambletidecare.example ONLY because I like the background of rich deep forest and the colors. If you think we it would look good to have fruits and vegetables as the background or border, then let me know if I should be sending you a photo or find one to use for now and get my opinion. Then the inside would be very very soft pale colors... pale lime green for example, pale magenta. Also I only referred to the website fernloftkitchen because I like the moderness of it and I like how the top words do NOT have boxes around them. But the letters are tooooo small. The grey is modern and interesting, but if we use grey it must be A LOT lighter and soft. I need for the doctors to be able to access the questions only with a password. We will have a link at the top that says Doctors Questionaire. They must be able to fill part of it out, save it and be able to return to the forms without losing all the data they put onto the questionaire. We need about 6 links at the top. I want the video for them to watch to be in the center or on the right side. Whatever you think looks best. The links at the top will say who we are, What we want to accomplish, What this book is about Why it is important you be a part of this well respected team ( I realize these are long, however we can shorten the phrases... maybe) and we will add a couple of more. You will see the logo. PLEASE make that BIG and at the top. ALSO, we have ANOTHER logo which is different that I will ALSO be using. I will upload the 2nd logo and the video next week. In the meantime please work only with the logo you have now. I have 2 fun logos to use for this website. PLEASE put the links that are at the top also on the bottom of the page too. When doctors click on to different pages I want to have these beautiful photos everywhere. You will see a photo with a little baby and LOTS of vegetables. Put that at the top of the page. Then a beautiful African American girl with food. Please put that also on the front page and ONE OTHER that has a doctor with food. Please put all of those on the front page and big. Thank you!! Meadow Healers WEBSITE

```html
<!DOCTYPE html>
<html lang="en">
<head>
<meta charset="utf-8">
<title>Meadow Healers</title>
<link rel="stylesheet" href="https://fonts.googleapis.com/css2?family=Open+Sans:wght@400;600;700;800&family=Nunito:wght@800&display=swap">
<style>
:root{
  --green:#5aa51f;
  --green-dark:#3f8a12;
  --green-pale:#eef6e2;
  --magenta:#a0267f;
  --ink:#2b2b2b;
  --grey:#666;
  --blue:#2f7fc1;
  --frame:#ffffff;
}
*{box-sizing:border-box;margin:0;padding:0}
html,body{width:1200px;height:919px;overflow:hidden}
body{font-family:"Open Sans",Arial,sans-serif;color:var(--ink);background:#fff;position:relative}
.backdrop{position:absolute;inset:0;background:
  radial-gradient(ellipse 260px 520px at 0% 55%,#cfe5b0 0%,rgba(207,229,176,0) 100%),
  radial-gradient(ellipse 260px 520px at 100% 50%,#e8d8b8 0%,rgba(232,216,184,0) 100%),
  linear-gradient(#f4faec,#fbfdf7 60%,#f3f8ea)}
.abs{position:absolute}
.brand{left:176px;top:24px;font-family:"Nunito",sans-serif;font-weight:800;color:var(--green);font-size:46px;line-height:48px;letter-spacing:1px}
.contact{left:600px;top:30px;width:345px;text-align:right}
.contact .phone{font-size:19px;font-weight:700;color:#333}
.contact .phone span{color:var(--magenta);font-weight:400}
.contact .mail{font-size:14px;font-weight:700;color:#333;margin-top:2px}
.contact .mail span{color:var(--magenta);font-weight:400}
.social{left:956px;top:32px;display:flex;gap:7px}
.social i{width:30px;height:30px;border-radius:50%;background:#3b9ad8;display:block}
.social i:nth-child(3){background:#2a6fa8}.social i:nth-child(4){background:#f08a24}
.nav{left:472px;top:106px;display:flex;font-size:9px;font-weight:700;text-transform:uppercase;color:#444}
.nav a{color:inherit;text-decoration:none;padding:9px 6px;border-right:1px solid #ccc;white-space:nowrap}
.nav a:last-child{border-right:0}
.nav a.active{background:var(--green);color:#fff}
.navline{left:472px;top:138px;width:560px;height:2px;background:linear-gradient(90deg,var(--green),#ddd)}
.hero{left:174px;top:174px;width:546px;height:303px;background:var(--frame);border-radius:6px;box-shadow:0 1px 8px rgba(0,0,0,.18);padding:8px}
.hero div{width:100%;height:100%;border-radius:3px;background:linear-gradient(#fff 0%,#fff 40%,#cde3a6 70%,#d86a3a 88%,#f3efe5 100%)}
.welcome{left:758px;top:228px;width:310px}
.welcome h2{font-weight:400;font-size:30px;color:#555;line-height:32px}
.welcome .brand-sm{font-family:"Nunito",sans-serif;font-weight:800;color:var(--green);font-size:26px;margin:2px 0 10px}
.welcome p{font-size:14px;line-height:19px;color:#333;margin-bottom:16px}
.section-title{left:174px;top:498px;font-size:17px;font-weight:700;color:#333}
.doctor{left:174px;top:529px;width:199px;height:211px;background:linear-gradient(#b7d6e6,#e9eef2 60%,#e07a3a);border-radius:3px}
.lorem{left:385px;top:529px;width:216px;font-size:11px;line-height:14px;color:#444}
.lorem em{font-style:normal;color:var(--green);font-weight:600}
.girl{left:611px;top:534px;width:109px;height:117px;background:linear-gradient(135deg,#d7d3cf,#8a5a3c 55%,#e8e2dc);border-radius:3px}
.news{left:385px;top:668px}
.news h3{font-size:22px;font-weight:800;color:var(--magenta);text-transform:uppercase;letter-spacing:.5px;line-height:26px}
.news p{font-size:10px;color:#555}
.signup{left:385px;top:718px;display:flex}
.signup .field{width:231px;height:22px;border:1px solid #ccc;background:#fff;font-size:10px;color:#999;padding:4px 6px}
.signup .btn{width:104px;height:22px;background:var(--green);color:#fff;font-size:10px;font-weight:700;text-align:center;line-height:22px;text-transform:uppercase}
.video{left:773px;top:512px;width:186px;height:145px;border:4px solid #fff;box-shadow:0 1px 6px rgba(0,0,0,.2);background:radial-gradient(circle at 40% 45%,#e5564a 0,#b53a3a 18%,#2a6fb8 40%,#bcd8ee 100%)}
.video svg{position:absolute;left:68px;top:50px}
.video-note{left:758px;top:688px;width:290px;font-size:12px;font-weight:700;line-height:17px;color:#333;text-transform:uppercase}
.swoosh{left:174px;top:757px}
.fnav{left:174px;top:862px;display:flex;font-size:10px;color:#333}
.fnav a{color:inherit;text-decoration:none;padding:0 6px;border-right:1px solid #999}
.fnav a:first-child{padding-left:0}.fnav a:last-child{border:0}
.copy{left:174px;top:882px;font-size:9px;color:#888}
.copy span{color:var(--magenta)}
.brand-foot{left:880px;top:840px;font-family:"Nunito",sans-serif;font-weight:800;color:var(--green);font-size:24px;line-height:25px;text-align:right}
</style>
</head>
<body>
<div class="backdrop" role="img" aria-label="Soft faded fruit and vegetable photography along both edges"></div>

<div class="abs brand">MEADOW<br>HEALERS</div>

<div class="abs contact">
  <div class="phone">Contact Us: <span>555.014.7890</span></div>
  <div class="mail">Email: <span>meadowhealers.example</span></div>
</div>
<div class="abs social" aria-label="Social links"><i></i><i></i><i></i><i></i></div>

<nav class="abs nav">
  <a class="active" href="#">Home</a>
  <a href="#">Who we are</a>
  <a href="#">What we want to accomplish</a>
  <a href="#">What this book is about</a>
  <a href="#">Why it is important</a>
</nav>
<div class="abs navline"></div>

<div class="abs hero"><div role="img" aria-label="Baby sitting among a large pile of fresh vegetables"></div></div>

<section class="abs welcome">
  <h2>welcome to</h2>
  <div class="brand-sm">MEADOW HEALERS</div>
  <p>This website will be used by medical doctors mainly in the United States and some from other parts of the world.</p>
  <p>These doctors all have lots of research and many years of experience with patients.</p>
</section>

<h2 class="abs section-title">What We Want To Accomplish</h2>
<div class="abs doctor" role="img" aria-label="Doctor in a white coat holding fresh vegetables"></div>
<p class="abs lorem">Sed ut perspiciatis unde omnis iste natus error sit voluptatem accusantium doloremque laudantium, totam rem aperiam, eaque ipsa quae ab illo inventore veritatis et quasi architecto beatae vitae dicta sunt explicabo. Sed quia consequ untur magni dolores <em>Neque porro quisquam est.</em></p>
<div class="abs girl" role="img" aria-label="Young woman enjoying a bowl of healthy food"></div>

<div class="abs news">
  <h3>Newsletter Signup</h3>
  <p>Subscribe to our mailing list</p>
</div>
<div class="abs signup"><div class="field">Email Address</div><div class="btn">Subscribe</div></div>

<div class="abs video" role="img" aria-label="Video still of a heart with a pulse line">
  <svg width="42" height="34" viewBox="0 0 50 40"><rect width="50" height="40" rx="8" fill="#222" opacity=".85"/><path d="M19 11 L34 20 L19 29Z" fill="#fff"/></svg>
</div>
<p class="abs video-note">Heque porro quisquam est qui doloreh ipsum quia dolor sit amet heque.</p>

<svg class="abs swoosh" width="852" height="100" viewBox="0 0 852 100">
  <path d="M0 10 Q420 80 852 10 L852 40 Q420 110 0 40Z" fill="#e6f1d6"/>
  <rect x="300" y="0" width="220" height="55" rx="20" fill="#8dbf4a" opacity=".55" role="img" aria-label="Row of fresh vegetables"/>
  <path d="M0 30 Q420 100 852 30" fill="none" stroke="var(--green)" stroke-width="12"/>
  <path d="M0 42 Q420 112 852 42" fill="none" stroke="var(--magenta)" stroke-width="5"/>
</svg>

<nav class="abs fnav">
  <a href="#">Home</a><a href="#">Who we are</a><a href="#">What we want to accomplish</a><a href="#">What this book is about</a><a href="#">Why it is important</a>
</nav>
<p class="abs copy">Copyright © meadowhealers.example. All Rights Reserved. | <span>Privacy Policy</span></p>
<div class="abs brand-foot">MEADOW<br>HEALERS</div>
</body>
</html>
```